Fun relaxed Travel Photography Business Card*

Require a fun, funky and quirky but rememberable business card for a travel photographer

Industry/Entity Type

Photographer

Contact Information for Business Card

Front Card

(my name) Tavo M.

Travel Photographer ( small under travel photographer) “self-proclaimed”

(website logo) wanderingtavo.example

(Instagram logo) @wandering_with_tavo

(Instagram logo) @wandering_with_tavo_2.0 (backup for when Instagram puts Tavo on timeout for bad behaviour)

Tel: N/A (removing the potential awkwardness of me not replying)

Email: (see above)

Back Card

Offending people since 1986

(Bottom right corner) “p.s. travelling made me fatTER”

Font styles to use
Serif

Colors

Designer to choose colors to be used in the design.

Requirements
Must have
• a camera
• a similar cartoon version of me as the "logo" see attached files, try to make as similar as possible

```html
<!DOCTYPE html>
<html lang="en">
<head>
<meta charset="utf-8">
<title>Tavo M. — Travel Photographer Business Card</title>
<link rel="stylesheet" href="https://fonts.googleapis.com/css2?family=Open+Sans:wght@400;600&display=swap">
<style>
  :root {
    --backdrop: #1f2226;
    --card-blue: #2b546f;
    --accent-yellow: #f1bd45;
    --text-white: #ffffff;
    --art-light: #f3b93c;
    --art-dark: #5a3a22;
  }
  * { margin: 0; padding: 0; box-sizing: border-box; }
  html, body {
    width: 1200px;
    height: 1200px;
    overflow: hidden;
    background: var(--backdrop);
    font-family: "Open Sans", Verdana, sans-serif;
  }
  .sheet {
    width: 1200px;
    height: 1200px;
    display: flex;
    flex-direction: column;
    align-items: center;
    justify-content: center;
    gap: 60px;
  }
  .card {
    position: relative;
    width: 900px;
    height: 514px;
    background: var(--card-blue);
    border-radius: 10px;
    overflow: hidden;
    box-shadow: 0 12px 30px rgba(0,0,0,0.45);
  }

  /* Front */
  .card-stripe {
    position: absolute;
    inset: 0;
    width: 100%;
    height: 100%;
  }
  .identity {
    position: absolute;
    left: 96px;
    top: 62px;
    line-height: 1.05;
  }
  .identity-name {
    color: var(--accent-yellow);
    font-size: 42px;
    font-weight: 400;
    letter-spacing: 1px;
  }
  .identity-title {
    color: var(--text-white);
    font-size: 31px;
    font-weight: 400;
    margin-top: 4px;
  }
  .identity-note {
    color: var(--text-white);
    font-size: 21px;
    margin-top: 2px;
  }
  .contacts {
    position: absolute;
    left: 300px;
    top: 356px;
    list-style: none;
  }
  .contact-item {
    display: flex;
    align-items: center;
    gap: 12px;
    height: 34px;
    color: var(--text-white);
    font-size: 18px;
  }
  .contact-dot {
    width: 16px;
    height: 16px;
    border-radius: 50%;
    background: var(--accent-yellow);
    flex: none;
  }
  .mascot-art {
    position: absolute;
    right: 24px;
    bottom: 18px;
    width: 190px;
    height: 230px;
    border-radius: 24px;
    background: linear-gradient(150deg, var(--art-light) 0%, #e0a232 60%, var(--art-dark) 100%);
  }

  /* Back */
  .tagline {
    position: absolute;
    left: 0;
    right: 0;
    top: 50%;
    transform: translateY(-50%);
    text-align: center;
    color: var(--accent-yellow);
    font-size: 46px;
    font-weight: 400;
    letter-spacing: 0.5px;
  }
  .corner-tab {
    position: absolute;
    width: 68px;
    height: 56px;
    border-radius: 10px;
    background: var(--accent-yellow);
    bottom: 36px;
  }
  .corner-tab--left { left: 36px; }
  .corner-tab--right { right: 36px; }
  .postscript {
    position: absolute;
    right: 124px;
    bottom: 48px;
    color: var(--accent-yellow);
    font-size: 19px;
  }
</style>
</head>
<body>
  <main class="sheet">
    <section class="card card--front">
      <svg class="card-stripe" viewBox="0 0 900 514" aria-hidden="true">
        <polygon points="0,96 0,128 318,514 356,514" fill="var(--accent-yellow)"/>
      </svg>
      <div class="identity">
        <h1 class="identity-name">TAVO M.</h1>
        <p class="identity-title">TRAVEL PHOTOGRAPHER</p>
        <p class="identity-note">self-proclaimed</p>
      </div>
      <ul class="contacts">
        <li class="contact-item"><span class="contact-dot"></span>wanderingtavo.example</li>
        <li class="contact-item"><span class="contact-dot"></span>@wandering_with_tavo</li>
        <li class="contact-item"><span class="contact-dot"></span>@wandering_with_tavo_2.0</li>
      </ul>
      <div class="mascot-art" role="img" aria-label="Cartoon mascot of Tavo in sunglasses and a patterned shirt lounging on a yellow beach chair beside a small table with a drink"></div>
    </section>

    <section class="card card--back">
      <p class="tagline">OFFENDING PEOPLE SINCE 1986</p>
      <span class="corner-tab corner-tab--left"></span>
      <span class="corner-tab corner-tab--right"></span>
      <p class="postscript">p.s. travelling made me fatTER</p>
    </section>
  </main>
</body>
</html>
```